Figma App design and working prototype

I need to create a User Interface design and a Working prototype using Figma or similar. I’d also like all the assets and guidelines needed to guide the App developers to create the final product.
So, I'll need Design files and assets but you that I can give to an App development company or a freelance developer to create Android and iOS apps.

This app is an app for adults who wan to meet and have sex no strings attached.

The App name will be Nuvora

I have attached an app some pictures and a pdf file explaining details of the apps functions.

This app will be a sexy version of the pobalo app with a personals section used for adult services. I have attached images and a pdf below that will tell you the functions of the app.

I need an app interface design done for an app idea I have. I am nee to this it is my first time trying to launch an app and I do not know what you need in order to get what I need. I need a site map/ design and if possible a working prototype that I can pass on to an app developer that can deliver the final product. This model will be used to raise funds and give investors an idea of what the apps functions will do as detailed in the project brief. Any advise would be greatly appreciated. Please let me know if you have any questions. Looking forward to working with you.

Target Market(s)

Adults men and women looking for some adult entertainment

Industry/Entity Type

Adult entertainment Strip clubs

Colors
E54698
E96AAD
F1A4CE
F9D9EA
FCEFF6
A7469A
B969AE
D3A5CF
EDDBEB
F8F0F9
6B429C
8869AF
B7A5CE
E3DAEB
F3F0F8

Requirements
Must have
• An 18+ confirmation,
Nice to have
• A sexy feel.

```html
<!DOCTYPE html>
<html lang="en">
<head>
<meta charset="utf-8">
<title>Nuvora — app screens</title>
<link href="https://fonts.googleapis.com/css2?family=Poppins:wght@400;500;600;700&display=swap" rel="stylesheet">
<style>
:root{
  --bg:#eddbeb;
  --pink:#e54698;
  --pink-2:#e96aad;
  --pink-3:#f1a4ce;
  --pink-4:#f9d9ea;
  --pink-5:#fceff6;
  --plum:#a7469a;
  --plum-2:#b969ae;
  --violet:#6b429c;
  --violet-2:#8869af;
  --lilac:#f3f0f8;
  --white:#ffffff;
  --ink:#1e1428;
  --muted:#8a7f93;
  --line:#e3daeb;
  --map:#d3a5cf;
  --map-2:#f8f0f9;
}
*{box-sizing:border-box;margin:0;padding:0}
html,body{width:1023px;height:1200px;overflow:hidden}
body{background:var(--bg);font-family:'Poppins',sans-serif;color:var(--ink);position:relative}
.screen{position:absolute;width:292px;border-radius:14px;overflow:hidden;background:var(--white)}
.abs{position:absolute}

/* age gate */
.gate{left:43px;top:69px;height:631px;background:linear-gradient(160deg,var(--pink),var(--plum) 60%,var(--violet));color:var(--white);text-align:center}
.gate .brand{position:absolute;left:0;right:0;top:168px;font-size:41px;font-weight:700;letter-spacing:-1px}
.gate .tagline{position:absolute;left:0;right:0;top:225px;font-size:14px;font-weight:600}
.gate .question{position:absolute;left:0;right:0;top:284px;font-size:13px}
.gate .choice{position:absolute;left:23px;width:246px;height:50px;background:var(--white);color:var(--ink);font-size:16px;font-weight:600;display:flex;align-items:center;justify-content:center;border-radius:2px}

/* shared header */
.status{position:absolute;left:0;right:0;top:0;height:39px;background:var(--pink);color:var(--white);font-size:13px;font-weight:600;padding:12px 14px}
.status .icons{position:absolute;right:14px;top:14px}
.appbar{position:absolute;left:0;right:0;top:39px;height:65px;background:linear-gradient(var(--plum),var(--violet));border-radius:0 0 14px 14px;color:var(--white);z-index:2}

/* home */
.home{left:366px;top:69px;height:950px;background:var(--pink-5)}
.home .brand{position:absolute;left:0;right:0;top:14px;text-align:center;font-size:26px;font-weight:700;letter-spacing:-.5px}
.cats{position:absolute;left:0;right:0;top:104px;height:78px;background:var(--white);border-bottom:2px solid var(--line)}
.cat{position:absolute;top:15px;width:60px;margin-left:-30px;text-align:center;font-size:7px;font-weight:500}
.cat .dot{width:34px;height:34px;border-radius:50%;border:1.5px solid var(--pink);margin:0 auto 4px;background:var(--pink-4);display:flex;align-items:center;justify-content:center}
.cat.more .dot{background:var(--pink-3);border:none}
.headline{position:absolute;left:16px;top:189px;font-size:15.5px;font-weight:600;line-height:21px}
.field{position:absolute;left:20px;width:252px;height:48px;border:1.5px solid var(--violet-2);border-radius:3px;padding:18px 14px 0;font-size:14px;font-weight:500}
.field .label{position:absolute;top:-9px;left:10px;background:var(--pink-5);padding:0 6px;font-size:11px;font-weight:400}
.field .caret{position:absolute;right:12px;top:19px}
.btn{position:absolute;background:var(--pink);color:var(--white);font-size:13px;font-weight:500;display:flex;align-items:center;justify-content:center;border-radius:2px}
.section{position:absolute;left:20px;font-size:13.5px;font-weight:500;color:var(--violet)}
.card{position:absolute;width:135px;height:137px;background:var(--white);box-shadow:0 1px 3px rgba(107,66,156,.18);overflow:hidden}
.card .photo{height:94px;position:relative}
.card .premium{position:absolute;left:2px;bottom:2px;background:var(--violet);color:var(--white);font-size:7.5px;padding:0 3px;border-radius:1px}
.card .ribbon{position:absolute;right:0;top:0;width:0;height:0;border-top:45px solid var(--pink);border-left:45px solid transparent}
.card .ribbon span{position:absolute;top:-38px;right:-2px;transform:rotate(45deg);color:var(--white);font-size:6.5px;font-style:italic}
.card .ago{position:absolute;left:8px;top:103px;font-size:5.5px}
.card .name{position:absolute;left:8px;top:111px;font-size:10px;font-weight:500;letter-spacing:.3px}
.card .heart{position:absolute;right:6px;top:114px}
.nav{position:absolute;left:0;right:0;top:899px;height:51px;background:var(--white);border-top:1px solid var(--line)}
.nav .item{position:absolute;top:10px;width:60px;margin-left:-30px;text-align:center;font-size:7.5px;color:var(--muted)}
.nav .post{position:absolute;left:119px;top:5px;width:40px;height:40px;border-radius:50%;background:var(--pink);color:var(--white);font-size:7.5px;text-align:center;padding-top:6px}

/* location */
.locate{left:702px;top:69px;height:631px}
.locate .title{position:absolute;left:51px;top:22px;font-size:15px;font-weight:500}
.map{position:absolute;left:0;right:0;top:100px;height:377px;background:linear-gradient(160deg,var(--map-2),var(--map))}
.searchbox{position:absolute;left:19px;top:133px;width:256px;height:42px;background:var(--white);padding:5px 10px;box-shadow:0 1px 3px rgba(107,66,156,.2)}
.searchbox small{display:block;font-size:7.5px;color:var(--muted)}
.searchbox b{font-size:13.5px;font-weight:500}
.pin{position:absolute;width:80px;height:31px;background:var(--white);border-radius:16px;box-shadow:0 1px 3px rgba(107,66,156,.25);padding:5px 0 0 33px;line-height:10px}
.pin .avatar{position:absolute;left:4px;top:4px;width:23px;height:23px;border-radius:50%}
.pin b{font-size:7.5px;font-weight:600;display:block}
.pin i{font-size:5.5px;font-style:normal;color:var(--muted)}
.region{position:absolute;left:18px;top:432px;width:156px;height:28px;background:var(--white);font-size:9px;padding:8px 0 0 28px;white-space:nowrap}
.region svg{position:absolute;left:9px;top:7px}
.dist{position:absolute;top:491px;font-size:12px;font-weight:500}
.dist.value{left:180px;top:487px;font-weight:400}
.slider{position:absolute;left:29px;top:525px;width:240px;height:2px;background:var(--violet)}
.thumb{position:absolute;left:185px;top:509px}
</style>
</head>
<body>

<section class="screen gate">
  <div class="brand">Nuvora</div>
  <div class="tagline">No.1 Escort Market Place</div>
  <div class="question">Are you 18+ years old?</div>
  <div class="choice" style="top:326px">Yes</div>
  <div class="choice" style="top:399px">NO</div>
</section>

<section class="screen home">
  <div class="status">04:20
    <svg class="icons" width="56" height="10" viewBox="0 0 56 10"><rect x="0" y="6" width="2" height="4" fill="#fff"/><rect x="3" y="4" width="2" height="6" fill="#fff"/><rect x="6" y="2" width="2" height="8" fill="#fff"/><rect x="9" y="0" width="2" height="10" fill="#fff"/><path d="M15 3a8 8 0 0 1 11 0M17 5.5a5 5 0 0 1 7 0" stroke="#fff" stroke-width="1.4" fill="none"/><circle cx="20.5" cy="8.5" r="1.2" fill="#fff"/><rect x="34" y="1" width="20" height="8" rx="1.5" fill="none" stroke="#fff"/><rect x="36" y="3" width="16" height="4" fill="#fff"/></svg>
  </div>
  <div class="appbar">
    <svg class="abs" style="left:20px;top:24px" width="18" height="16" viewBox="0 0 18 16"><path d="M0 1h18M0 8h18M0 15h18" stroke="#fff" stroke-width="1.5"/></svg>
    <div class="brand">Nuvora</div>
  </div>

  <div class="cats">
    <div class="cat" style="left:37px"><div class="dot"></div>Escorts</div>
    <div class="cat" style="left:87px"><div class="dot"></div>Sex Toys</div>
    <div class="cat" style="left:145px"><div class="dot"></div>Virtual Escorts</div>
    <div class="cat" style="left:199px"><div class="dot"></div>Party</div>
    <div class="cat more" style="left:255px"><div class="dot"><svg width="14" height="10" viewBox="0 0 14 10"><path d="M0 5h12M8 1l4 4-4 4" stroke="#a7469a" stroke-width="1.4" fill="none"/></svg></div>All Categories</div>
  </div>

  <div class="headline">Get Nuvora with your next<br>Escort, search below</div>

  <div class="field" style="top:256px"><span class="label">Search Provice</span>Pickering, ON
    <svg class="caret" width="8" height="9" viewBox="0 0 8 9"><path d="M0 0l8 4.5L0 9z" fill="#8869af"/></svg></div>
  <div class="field" style="top:329px"><span class="label">Select Preferred Escort</span>Female Escort
    <svg class="caret" width="10" height="8" viewBox="0 0 10 8"><path d="M0 0h10L5 8z" fill="#8869af"/></svg></div>
  <div class="btn" style="left:20px;top:398px;width:254px;height:41px">SEARCH</div>

  <div class="section" style="top:480px">TOP 10 ESCORT GIRLS</div>
  <div class="card" style="left:20px;top:515px">
    <div class="photo" role="img" aria-label="Profile photo of a female escort" style="background:linear-gradient(135deg,#8a5a44,#d9a48a)"><span class="premium">Premium</span><div class="ribbon"><span>Verified</span></div></div>
    <span class="ago">1hr ago</span><span class="name">ANASTASIA _25</span>
    <svg class="heart" width="12" height="11" viewBox="0 0 12 11"><path d="M6 10S1 7 1 3.5A2.5 2.5 0 0 1 6 2a2.5 2.5 0 0 1 5 1.5C11 7 6 10 6 10z" fill="none" stroke="#b969ae"/></svg>
  </div>
  <div class="card" style="left:163px;top:515px">
    <div class="photo" role="img" aria-label="Profile photo of a female escort" style="background:linear-gradient(135deg,#c9a27c,#f1dcc4)"><span class="premium">Premium</span><div class="ribbon"><span>Verified</span></div></div>
    <span class="ago">1hr ago</span><span class="name">ANASTASIA _25</span>
    <svg class="heart" width="12" height="11" viewBox="0 0 12 11"><path d="M6 10S1 7 1 3.5A2.5 2.5 0 0 1 6 2a2.5 2.5 0 0 1 5 1.5C11 7 6 10 6 10z" fill="none" stroke="#b969ae"/></svg>
  </div>

  <div class="section" style="top:681px">TOP 10 ESCORT GUYS</div>
  <div class="card" style="left:20px;top:716px">
    <div class="photo" role="img" aria-label="Profile photo of a male escort" style="background:linear-gradient(135deg,#6b4530,#c78d6a)"><span class="premium">Premium</span><div class="ribbon"><span>Verified</span></div></div>
    <span class="ago">1hr ago</span><span class="name">Vagila1993</span>
    <svg class="heart" width="12" height="11" viewBox="0 0 12 11"><path d="M6 10S1 7 1 3.5A2.5 2.5 0 0 1 6 2a2.5 2.5 0 0 1 5 1.5C11 7 6 10 6 10z" fill="none" stroke="#b969ae"/></svg>
  </div>
  <div class="card" style="left:163px;top:716px">
    <div class="photo" role="img" aria-label="Profile photo of a male escort outdoors" style="background:linear-gradient(135deg,#3d5a2e,#b98a6a)"><span class="premium">Premium</span><div class="ribbon"><span>Verified</span></div></div>
    <span class="ago">1hr ago</span><span class="name">Dante Hetero</span>
    <svg class="heart" width="12" height="11" viewBox="0 0 12 11"><path d="M6 10S1 7 1 3.5A2.5 2.5 0 0 1 6 2a2.5 2.5 0 0 1 5 1.5C11 7 6 10 6 10z" fill="none" stroke="#b969ae"/></svg>
  </div>

  <nav class="nav">
    <div class="item" style="left:29px"><svg width="14" height="13" viewBox="0 0 14 13"><path d="M1 6L7 1l6 5v6H1z" fill="none" stroke="#8a7f93"/></svg><br>Home</div>
    <div class="item" style="left:83px"><svg width="13" height="13" viewBox="0 0 13 13"><circle cx="6.5" cy="4" r="3" fill="none" stroke="#8a7f93"/><path d="M1 12.5a5.5 4 0 0 1 11 0z" fill="none" stroke="#8a7f93"/></svg><br>Profile</div>
    <div class="post"><svg width="12" height="12" viewBox="0 0 12 12"><circle cx="6" cy="6" r="5" fill="none" stroke="#fff"/><path d="M6 3.5v5M3.5 6h5" stroke="#fff"/></svg><br>Post</div>
    <div class="item" style="left:197px"><svg width="14" height="13" viewBox="0 0 12 11"><path d="M6 10S1 7 1 3.5A2.5 2.5 0 0 1 6 2a2.5 2.5 0 0 1 5 1.5C11 7 6 10 6 10z" fill="none" stroke="#8a7f93"/></svg><br>Favorites</div>
    <div class="item" style="left:258px"><svg width="14" height="13" viewBox="0 0 14 13"><path d="M1 2h12v7H5l-3 3V9H1z" fill="none" stroke="#8a7f93"/></svg><br>Messeges</div>
  </nav>
</section>

<section class="screen locate">
  <div class="map" role="img" aria-label="Road map of southwestern Ontario"></div>
  <div class="status">04:20
    <svg class="icons" width="56" height="10" viewBox="0 0 56 10"><rect x="0" y="6" width="2" height="4" fill="#fff"/><rect x="3" y="4" width="2" height="6" fill="#fff"/><rect x="6" y="2" width="2" height="8" fill="#fff"/><rect x="9" y="0" width="2" height="10" fill="#fff"/><path d="M15 3a8 8 0 0 1 11 0M17 5.5a5 5 0 0 1 7 0" stroke="#fff" stroke-width="1.4" fill="none"/><circle cx="20.5" cy="8.5" r="1.2" fill="#fff"/><rect x="34" y="1" width="20" height="8" rx="1.5" fill="none" stroke="#fff"/><rect x="36" y="3" width="16" height="4" fill="#fff"/></svg>
  </div>
  <div class="appbar">
    <svg class="abs" style="left:20px;top:27px" width="20" height="12" viewBox="0 0 20 12"><path d="M20 6H2M7 1L2 6l5 5" stroke="#fff" stroke-width="1.5" fill="none"/></svg>
    <div class="title">Choose Location</div>
  </div>

  <div class="searchbox"><small>Search location</small><b>Pickering, ON</b>
    <svg class="abs" style="right:12px;top:14px" width="14" height="14" viewBox="0 0 14 14"><circle cx="6" cy="6" r="5" fill="none" stroke="#1e1428"/><path d="M10 10l3.5 3.5" stroke="#1e1428"/></svg></div>

  <div class="pin" style="left:189px;top:196px"><span class="avatar" role="img" aria-label="Profile photo" style="background:#c99a7e"></span><b>Gracexxx</b><i>Listowe</i></div>
  <div class="pin" style="left:62px;top:234px"><span class="avatar" role="img" aria-label="Profile photo" style="background:#d8b596"></span><b>Messlisa</b><i>Listowe</i></div>
  <div class="pin" style="left:160px;top:265px"><span class="avatar" role="img" aria-label="Profile photo" style="background:#e0a9a0"></span><b>Gracexxx</b><i>Listowe</i></div>
  <div class="pin" style="left:40px;top:317px"><span class="avatar" role="img" aria-label="Profile photo" style="background:#a87a62"></span><b>Jennifa</b><i>Listowe</i></div>
  <div class="pin" style="left:154px;top:346px"><span class="avatar" role="img" aria-label="Profile photo" style="background:#5b4a42"></span><b>Michael</b><i>Listowe</i></div>
  <div class="pin" style="left:37px;top:390px"><span class="avatar" role="img" aria-label="Profile photo" style="background:#5b4a42"></span><b>Michael</b><i>Listowe</i></div>
  <div class="pin" style="left:186px;top:417px"><span class="avatar" role="img" aria-label="Profile photo" style="background:#5b4a42"></span><b>Michael</b><i>Listowe</i></div>

  <div class="region"><svg width="12" height="12" viewBox="0 0 12 12"><rect x=".5" y=".5" width="11" height="11" fill="#fff" stroke="#d3a5cf"/><path d="M2.5 6l2.5 2.5 4.5-5" stroke="#6b429c" stroke-width="1.3" fill="none"/></svg>Search all Ontario region</div>

  <div class="dist" style="left:27px">DISTANCE</div>
  <div class="dist value">150km</div>
  <div class="slider"></div>
  <svg class="thumb" width="28" height="34" viewBox="0 0 28 34"><path d="M14 33L4 22A13 13 0 1 1 24 22z" fill="#fff" stroke="#6b429c" stroke-width="2"/><path d="M9 11h10M9 15h10M9 19h10" stroke="#6b429c" stroke-width="2"/></svg>
  <div class="btn" style="left:27px;top:555px;width:239px;height:37px">APPLY</div>
</section>

</body>
</html>
```